Wholesale in Gold Jewellery & Gold Bullion

We are an established gold jewellery and gold bullion wholesaler selling these products to international clients. We already have a name and logo of our company, hence please view attached current card design. We need a completely new design to compliment our business and industry and the final design should be new and elegant.

Contact Information for Business Card

New card details must be same as per current card. Like logo, name, tel no. & etc.

Colors

Designer to choose colors to be used in the design.

```html
<!DOCTYPE html>
<html lang="en">
<head>
<meta charset="utf-8">
<title>Aurelian &amp; Co – Business Card</title>
<link rel="stylesheet" href="https://fonts.googleapis.com/css2?family=Tinos:wght@700&family=PT+Sans:wght@400;700&display=swap">
<style>
  :root {
    --card-black: #050505;
    --gold: #d4901e;
    --ink-white: #ffffff;
    --backdrop: #e8e5e0;
  }
  * { box-sizing: border-box; margin: 0; padding: 0; }
  html, body {
    width: 1200px;
    height: 900px;
    overflow: hidden;
    background: var(--backdrop);
  }
  .business-card {
    position: absolute;
    left: 150px;
    top: 180px;
    width: 900px;
    height: 540px;
    background: var(--card-black);
    overflow: hidden;
    box-shadow: 0 10px 30px rgba(0,0,0,0.18);
    font-family: "PT Sans", sans-serif;
    color: var(--ink-white);
  }
  .gold-band {
    position: absolute;
    inset: 0;
    width: 100%;
    height: 100%;
  }
  .brand {
    position: absolute;
    left: 60px;
    top: 100px;
    display: flex;
    align-items: center;
    gap: 26px;
  }
  .brand-dot {
    width: 100px;
    height: 100px;
    border-radius: 50%;
    background: var(--gold);
  }
  .brand-name {
    font-family: "Tinos", serif;
    font-weight: 700;
    font-size: 38px;
    letter-spacing: 0.5px;
    color: var(--ink-white);
    margin-top: -40px;
  }
  .address {
    position: absolute;
    left: 395px;
    top: 212px;
    font-size: 20px;
  }
  .contact-list {
    position: absolute;
    left: 405px;
    top: 248px;
    display: grid;
    grid-template-columns: 112px auto;
    row-gap: 2px;
    font-size: 20px;
    line-height: 1.3;
  }
  .contact-label { font-weight: 700; }
  .name-plate {
    position: absolute;
    left: 80px;
    top: 300px;
    width: 300px;
    height: 92px;
    background: var(--gold);
    padding: 20px 24px;
    line-height: 1.25;
  }
  .person-name { font-weight: 700; font-size: 22px; }
  .person-title { font-size: 19px; }
</style>
</head>
<body>
  <div class="business-card">
    <svg class="gold-band" viewBox="0 0 900 540" preserveAspectRatio="none" aria-hidden="true">
      <polygon points="0,425 495,490 900,270 900,540 0,540" fill="var(--gold)"/>
    </svg>

    <div class="brand">
      <div class="brand-dot"></div>
      <div class="brand-name">AURELIAN &amp; CO PTE LTD</div>
    </div>

    <p class="address">52 Lorne Crescent, Singapore 208110</p>

    <div class="contact-list">
      <span class="contact-label">Telephone</span><span>: +65 6000 1234</span>
      <span class="contact-label">Fax</span><span>: +65 6000 5678</span>
      <span class="contact-label">Mobile</span><span>: +65 9000 2468</span>
      <span class="contact-label">Email</span><span>: rohan@aurelianco.com</span>
    </div>

    <div class="name-plate">
      <p class="person-name">Rohan Mehrotra</p>
      <p class="person-title">Director</p>
    </div>
  </div>
</body>
</html>
```